Business Cards for Harbourline Coatings Pty Ltd

Hi every one i need a design for my buisness cards. I Want my logo in it and the name of the company needs to stand out Harbourline Coatings Pty Ltd. I want the background of the buisness cards black and i want the font to stand out in either a white or a silver stylish text. I want the design to be simple but original not to in your face if you know what i mean. I want on the back of the buisness cards to have the services that my buisness offers.
• Interior/Exterior
• Residential/Commercial
• Special effects/Texture Coatings
• Water Damage Repair
• Fully qualified
• Pensioner Discount
• 10 Year guarantee
• Fully Insured
• Obligation free quotes
full internal repaints include a proffesionla cleaning service
I want the services on the back to be layed out in an originall way not just dot points. If possible could my logo take up the whole back ground of the back but the text with the services be kind of like transparent so u cvan still see the logo i dont know if its possible it woiuld just look cool if possible. When i pick a design ill give my contact details to the designer to add to the design at the end. Any questions please just ask! Ill upload my logo.
Conatcs will include office phone: Mobile: E-mail - dale@harbourlinecoatings.com.au, Ill also have a Postal address which is a PO Box and my website is www.harbourlinecoatings.com.au

```html
<!DOCTYPE html>
<html lang="en">
<head>
<meta charset="utf-8">
<title>Harbourline Coatings – Business Cards</title>
<link href="https://fonts.googleapis.com/css2?family=Courier+Prime:wght@400;700&family=Roboto+Condensed:wght@700&display=swap" rel="stylesheet">
<style>
  :root {
    --backdrop: #8a8c89;
    --card-black: #1c1c1c;
    --silver-light: #e6e6e6;
    --silver-mid: #a9a9a9;
    --silver-dark: #5f5f5f;
    --brand-green: #8dc63f;
    --text-white: #ffffff;
    --text-soft: #e8e8e8;
  }
  * { box-sizing: border-box; margin: 0; padding: 0; }
  html, body {
    width: 1200px; height: 709px; overflow: hidden;
    background: var(--backdrop);
  }
  .canvas { position: relative; width: 1200px; height: 709px; }

  .card {
    position: absolute; top: 218px;
    width: 505px; height: 279px;
    border-radius: 10px; overflow: hidden;
    background: var(--card-black);
  }
  .card--back  { left: 71px; }
  .card--front { left: 624px; }

  .card__top-band {
    position: absolute; left: 0; top: 0; width: 100%; height: 26px;
    background: linear-gradient(90deg, var(--silver-dark) 0%, var(--silver-mid) 30%, var(--silver-light) 55%, var(--silver-mid) 80%, var(--silver-dark) 100%);
  }
  .card__bottom-band {
    position: absolute; left: 0; bottom: 0; width: 100%; height: 33px;
    background: linear-gradient(90deg, var(--silver-dark) 0%, var(--silver-mid) 25%, var(--silver-light) 50%, var(--silver-mid) 75%, var(--silver-dark) 100%);
    display: flex; align-items: center; justify-content: center;
  }
  .card__shade {
    position: absolute; left: 0; top: 26px; width: 100%; height: 220px;
    background: linear-gradient(180deg, rgba(0,0,0,0.35) 0%, rgba(0,0,0,0) 20%, rgba(255,255,255,0.04) 70%, rgba(0,0,0,0.2) 100%);
  }

  .brand {
    position: absolute; left: 20px; top: 38px;
    display: flex; flex-direction: column; align-items: flex-start;
  }
  .brand__square {
    width: 38px; height: 38px; margin-left: 46px;
    background: var(--brand-green); border-radius: 3px;
  }
  .brand__name {
    margin-top: 7px;
    font-family: "Roboto Condensed", "Arial Narrow", sans-serif;
    font-weight: 700; font-size: 15px; line-height: 18px;
    color: var(--text-white); letter-spacing: 0.2px;
  }

  .services {
    position: absolute; left: 17px; top: 152px; width: 475px;
    font-family: "Courier Prime", "Courier New", monospace;
    font-weight: 700; font-size: 12.4px; line-height: 20px;
    color: var(--text-white);
  }
  .services__item--accent { color: var(--brand-green); }

  .web-address {
    font-family: "Courier Prime", "Courier New", monospace;
    font-weight: 700; font-size: 13px; color: var(--text-white);
    text-shadow: 0 1px 1px rgba(0,0,0,0.5);
  }

  .person {
    position: absolute; left: 26px; top: 138px;
    font-family: "Courier Prime", "Courier New", monospace;
  }
  .person__name { font-size: 17px; font-weight: 400; color: var(--brand-green); line-height: 20px; letter-spacing: 0.5px; }
  .person__role { font-size: 12.5px; font-weight: 700; color: var(--text-white); line-height: 18px; }

  .contact {
    position: absolute; right: 18px; top: 160px;
    text-align: right; list-style: none;
    font-family: "Courier Prime", "Courier New", monospace;
    font-size: 11px; line-height: 12.5px; color: var(--text-soft);
  }
</style>
</head>
<body>
<main class="canvas">

  <section class="card card--back" aria-label="Business card back – services">
    <div class="card__top-band"></div>
    <div class="card__shade"></div>
    <div class="brand">
      <span class="brand__square"></span>
      <span class="brand__name">HARBOURLINE COATINGS</span>
    </div>
    <p class="services">
      <span class="services__item--accent">Interior/Exterior | Residential/Commercial | Special effects/ Texture Coatings | Water Damage Repair |</span>
      Fully qualified Pensioner Discount | 10 Year guarantee | Fully Insured | Obligation free quotes
    </p>
    <div class="card__bottom-band">
      <span class="web-address">www.harbourlinecoatings.com.au</span>
    </div>
  </section>

  <section class="card card--front" aria-label="Business card front – contact">
    <div class="card__top-band"></div>
    <div class="card__shade"></div>
    <div class="brand">
      <span class="brand__square"></span>
      <span class="brand__name">HARBOURLINE COATINGS</span>
    </div>
    <div class="person">
      <p class="person__name">DALE</p>
      <p class="person__role">Managing Director</p>
    </div>
    <ul class="contact">
      <li>Harbourline Coatings Pty Ltd</li>
      <li>PO Box 4821, Kingsford NSW 2032</li>
      <li>Tel : +02-5550-1842</li>
      <li>0400-555-318</li>
      <li>dale@harbourlinecoatings.com.au</li>
      <li>www.harbourlinecoatings.com.au</li>
    </ul>
    <div class="card__bottom-band"></div>
  </section>

</main>
</body>
</html>
```